Dale Merrow Broker owner of Real Estate Company

Dale Merrow, HQD LMV TRC
Broker Owner
586-317-4902
dalemerrow@dalemerrowrealtors.example
14637 Larkspur Ave. Bayview Harbor, MI 48297
Licensed in Michigan and Florida
"36 Years of Dependable Service built on a Client Focused Marketing Approach"

```html
<!DOCTYPE html>
<html lang="en">
<head>
<meta charset="utf-8">
<title>Dale Merrow – Business Card</title>
<link href="https://fonts.googleapis.com/css2?family=Montserrat:wght@400;500;700&display=swap" rel="stylesheet">
<style>
  :root {
    --backdrop: #e7e3de;
    --card: #1b1b1b;
    --gold: #e9b15e;
    --ink-light: #f4f1ec;
    --photo-top: #6f7570;
    --photo-bottom: #3a3d44;
  }
  * { margin: 0; padding: 0; box-sizing: border-box; }
  html, body {
    width: 1200px; height: 848px; overflow: hidden;
    background: var(--backdrop);
    font-family: "Montserrat", sans-serif;
  }
  .stage { position: relative; width: 1200px; height: 848px; }
  .card {
    position: absolute; top: 127px;
    width: 335px; height: 585px;
    background: var(--card);
    box-shadow: 0 6px 18px rgba(0,0,0,.18);
  }
  .card--front { left: 242px; }
  .card--back { left: 612px; }

  .portrait {
    position: absolute; left: 82px; top: 66px;
    width: 169px; height: 169px;
    background: linear-gradient(160deg, var(--photo-top), var(--photo-bottom));
  }
  .front-text { position: absolute; left: 0; width: 100%; text-align: center; }
  .agent-name {
    top: 259px; font-weight: 700; font-size: 20px; color: var(--gold);
    letter-spacing: .2px;
  }
  .agent-title { top: 284px; font-size: 13.5px; color: var(--ink-light); }
  .agent-license { top: 301px; font-size: 13.5px; color: var(--gold); }

  .icon { position: absolute; }
  .icon--pin { left: 157px; top: 389px; }
  .address { top: 416px; font-size: 13.5px; line-height: 18.5px; color: var(--ink-light); }
  .contact-icons { position: absolute; top: 470px; left: 131px; display: flex; gap: 4px; }
  .contacts { top: 501px; font-size: 13.5px; line-height: 19px; color: var(--ink-light); }

  .tagline {
    position: absolute; left: 50%; top: 46px;
    transform: translateX(-50%);
    writing-mode: vertical-rl;
    font-weight: 700; font-size: 12.6px; color: var(--gold);
    white-space: nowrap;
  }
</style>
</head>
<body>
<main class="stage">
  <section class="card card--front">
    <div class="portrait" role="img" aria-label="Portrait photo of Dale Merrow"></div>
    <h1 class="front-text agent-name">Dale Merrow, HQD LMV TRC</h1>
    <p class="front-text agent-title">Broker Owner</p>
    <p class="front-text agent-license">Licensed in Michigan and Florida</p>

    <svg class="icon icon--pin" width="21" height="21" viewBox="0 0 22 22" aria-hidden="true">
      <circle cx="11" cy="11" r="10" fill="none" stroke="var(--gold)" stroke-width="1.4"/>
      <path d="M11 5.2a3.6 3.6 0 0 0-3.6 3.6c0 2.7 3.6 7 3.6 7s3.6-4.3 3.6-7A3.6 3.6 0 0 0 11 5.2z" fill="var(--gold)"/>
      <circle cx="11" cy="8.8" r="1.3" fill="var(--card)"/>
    </svg>
    <p class="front-text address">14637 Larkspur Ave.<br>Bayview Harbor, MI 48297</p>

    <div class="contact-icons" aria-hidden="true">
      <svg width="22" height="22" viewBox="0 0 22 22">
        <circle cx="11" cy="11" r="10" fill="none" stroke="var(--gold)" stroke-width="1.4"/>
        <path d="M7.3 6.2l2 .1.9 2.3-1.1.9a6 6 0 0 0 2.6 2.6l.9-1.1 2.3.9.1 2a1.3 1.3 0 0 1-1.4 1.2A8 8 0 0 1 6 7.6a1.3 1.3 0 0 1 1.3-1.4z" fill="none" stroke="var(--gold)" stroke-width="1.2"/>
      </svg>
      <svg width="22" height="22" viewBox="0 0 22 22">
        <circle cx="11" cy="11" r="10" fill="none" stroke="var(--gold)" stroke-width="1.4"/>
        <rect x="6" y="7.5" width="10" height="7" rx=".6" fill="var(--gold)"/>
        <path d="M6.3 8l4.7 3.6L15.7 8" fill="none" stroke="var(--card)" stroke-width="1"/>
      </svg>
      <svg width="22" height="22" viewBox="0 0 22 22">
        <circle cx="11" cy="11" r="10" fill="none" stroke="var(--gold)" stroke-width="1.4"/>
        <g fill="none" stroke="var(--gold)" stroke-width="1">
          <circle cx="11" cy="11" r="5.5"/>
          <ellipse cx="11" cy="11" rx="2.4" ry="5.5"/>
          <path d="M5.5 11h11M6.3 8.2h9.4M6.3 13.8h9.4"/>
        </g>
      </svg>
    </div>
    <p class="front-text contacts">586-317-4902<br>dalemerrow@dalemerrowrealtors.example<br>www.dalemerrowrealtors.example</p>
  </section>

  <section class="card card--back">
    <p class="tagline">36 Years of Dependable Service built on a Client Focused Marketing Approach</p>
  </section>
</main>
</body>
</html>
```